Water Bottle Design

We are launching a water bottle and need a impactful design.

Target Market(s)

health conscious hipsters

Font styles to use
Sans Serif

Requirements
Must have
• Please include the logo (included) on one side of the bottle and these words on the other side of the bottle. "It’s simple, REUSE this bottle every day. Your action, will REDUCE the amount of waste produced. SAVE your body from drinking the harmful contaminants in your water from Non-BPA plastics. HELP someone else because proceeds from your purchase will help homeless veterans.
• We’re just two dudes that like to drink water and help people. #PayItFoward"
• Use a total of two colors
• UPDATE: You do not have to use the bottle on the logo.
Nice to have
• The bottle itself is 34 ounces and looks like a normal water bottle. I will include the image in the files. We would need to be able to change the colors easily.
Should not have
• Do not use more than two colors. Colors should not be important to the design at this point.

```html
<!DOCTYPE html>
<html lang="en">
<head>
<meta charset="utf-8">
<title>Bottle Wrap Labels</title>
<link rel="stylesheet" href="https://fonts.googleapis.com/css2?family=Oswald:wght@300;400;600&display=swap">
<style>
  :root {
    --bg: #eef1f4;
    --label-blue: #7fcdf0;
    --ink: #14202c;
    --white: #ffffff;
  }
  * { box-sizing: border-box; margin: 0; padding: 0; }
  html, body {
    width: 1200px; height: 1101px; overflow: hidden;
    background: var(--bg);
    font-family: "Oswald", "Arial Narrow", sans-serif;
  }
  .canvas {
    position: relative; width: 1200px; height: 1101px;
    display: flex; justify-content: center; align-items: center; gap: 60px;
  }
  .label {
    position: relative; width: 320px; height: 900px;
    background: var(--label-blue);
  }

  /* Message side */
  .message-side { padding: 40px 34px; color: var(--ink); }
  .rule { height: 4px; background: var(--ink); margin-bottom: 8px; }
  .rule.thin { height: 2px; }
  .intro { display: flex; flex-direction: column; align-items: center; margin: 40px 0 46px; }
  .intro svg { display: block; margin-bottom: 4px; }
  .intro-badge {
    background: var(--ink); color: var(--white);
    font-weight: 400; font-size: 22px; letter-spacing: 3px;
    padding: 6px 22px; text-transform: uppercase;
  }
  .step { margin-bottom: 44px; }
  .step-title {
    background: var(--white); color: var(--ink);
    text-align: center; font-weight: 600; font-size: 30px;
    letter-spacing: 6px; line-height: 1.35; text-transform: uppercase;
    margin-bottom: 14px;
  }
  .step-text {
    font-weight: 400; font-size: 17px; line-height: 1.2;
    text-transform: uppercase; letter-spacing: 0.3px;
  }
  .closing-rules { position: absolute; left: 34px; right: 34px; bottom: 40px; }

  /* Brand side */
  .brand-side { overflow: hidden; }
  .brand-dot {
    position: absolute; left: 50%; top: 150px; transform: translateX(-50%);
    width: 96px; height: 96px; border-radius: 50%; background: var(--white);
  }
  .brand-lockup {
    position: absolute; left: 50%; top: 640px;
    transform: translate(-50%, -50%) rotate(-90deg);
    display: flex; align-items: flex-end; gap: 18px;
    color: var(--white); font-weight: 300; white-space: nowrap;
  }
  .brand-name { font-size: 190px; line-height: 0.8; letter-spacing: 4px; }
  .brand-tagline { font-size: 34px; line-height: 1; padding-bottom: 6px; }
</style>
</head>
<body>
<main class="canvas">

  <section class="label message-side" aria-label="Bottle message side">
    <div class="rule"></div>
    <div class="rule thin"></div>

    <div class="intro">
      <svg width="90" height="26" viewBox="0 0 90 26" aria-hidden="true">
        <g stroke="#14202c" stroke-width="2.5" stroke-linecap="round">
          <line x1="45" y1="2" x2="45" y2="20"/>
          <line x1="30" y1="6" x2="36" y2="20"/>
          <line x1="60" y1="6" x2="54" y2="20"/>
          <line x1="16" y1="12" x2="26" y2="22"/>
          <line x1="74" y1="12" x2="64" y2="22"/>
        </g>
      </svg>
      <div class="intro-badge">It's Simple</div>
    </div>

    <div class="step">
      <h2 class="step-title">Reuse</h2>
      <p class="step-text">The bottle every day.<br>Your action will</p>
    </div>
    <div class="step">
      <h2 class="step-title">Reduce</h2>
      <p class="step-text">The amount<br>of waste produced.</p>
    </div>
    <div class="step">
      <h2 class="step-title">Save</h2>
      <p class="step-text">Your body from drinking the harmful contaminants in your water from Non-BPA plastics.</p>
    </div>
    <div class="step">
      <h2 class="step-title">Help</h2>
      <p class="step-text">Someone else because proceeds from your purchase will help homeless veterans.</p>
    </div>

    <div class="closing-rules">
      <div class="rule thin"></div>
      <div class="rule"></div>
    </div>
  </section>

  <section class="label brand-side" aria-label="Bottle brand side">
    <div class="brand-dot"></div>
    <div class="brand-lockup">
      <span class="brand-name">TAO</span>
      <span class="brand-tagline">Tap It Onward</span>
    </div>
  </section>

</main>
</body>
</html>
```